Larkvale Residences Stationery Design Project

Simple with logo at top, address and contact information along bottom.
Hi Designers: If interested, this Stationery project is linked to Business Card Project:
http://gigs.brieftable.example/task.aspx?id=517264
Updates

Project Deadline Extended
Reason: I would like to see the business card & letterhead coordinated.

Target Market(s)

Professional renters and white color families in a suburban area of the midwest

Industry/Entity Type

Business

Colors
fece3e
fbee3f
add136
34b8a4
34a7d8
3176b5
faa54b

Requirements
Must have
• logo at top, simple not fussy font
Should not have
• shading and graduated hard to copy color

```html
<!DOCTYPE html>
<html lang="en">
<head>
<meta charset="utf-8">
<title>Larkvale Residences – Business Card</title>
<link href="https://fonts.googleapis.com/css2?family=Arimo:wght@400&display=swap" rel="stylesheet">
<style>
  :root {
    --card-black: #000000;
    --lime: #add136;
    --lime-bright: #b6f23a;
    --sky-blue: #34a7d8;
    --deep-blue: #1f4fa8;
    --navy: #14307a;
    --sun: #faa54b;
    --text-white: #ffffff;
    --text-grey: #9a9a9a;
  }
  html, body {
    margin: 0;
    padding: 0;
    width: 1200px;
    height: 686px;
    overflow: hidden;
    background: var(--card-black);
  }
  .business-card {
    position: relative;
    width: 1200px;
    height: 686px;
    background: var(--card-black);
    overflow: hidden;
    font-family: "Arimo", Arial, sans-serif;
  }
  .stripes {
    position: absolute;
    inset: 0;
  }
  .brand {
    position: absolute;
    left: 66px;
    top: 34px;
    display: flex;
    align-items: center;
    gap: 14px;
    color: var(--text-white);
  }
  .brand-dot {
    width: 30px;
    height: 30px;
    border-radius: 50%;
    background: var(--sun);
  }
  .brand-name {
    font-size: 40px;
    line-height: 1.05;
    font-weight: 400;
    letter-spacing: 1px;
  }
  .brand-name span {
    display: block;
    font-size: 22px;
    letter-spacing: 8px;
  }
  .contact {
    position: absolute;
    left: 0;
    width: 1020px;
    top: 508px;
    text-align: center;
  }
  .contact p {
    margin: 0;
    line-height: 1.12;
  }
  .contact-heading {
    color: var(--text-white);
    font-size: 35px;
  }
  .contact-address {
    color: var(--text-grey);
    font-size: 31px;
  }
  .contact-phone {
    color: var(--text-white);
    font-size: 31px;
  }
  .website {
    position: absolute;
    left: 56px;
    top: 618px;
    color: var(--text-grey);
    font-size: 30px;
    letter-spacing: 26px;
    white-space: nowrap;
  }
</style>
</head>
<body>
  <div class="business-card">
    <svg class="stripes" width="1200" height="686" viewBox="0 0 1200 686" aria-hidden="true">
      <defs>
        <linearGradient id="blueBand" x1="0" y1="0" x2="1" y2="1">
          <stop offset="0" stop-color="var(--sky-blue)"/>
          <stop offset="1" stop-color="var(--deep-blue)"/>
        </linearGradient>
      </defs>
      <polygon fill="var(--lime-bright)" points="680,0 737,0 -175,686 -232,686"/>
      <polygon fill="url(#blueBand)" points="754,0 790,0 -122,686 -158,686"/>
      <polygon fill="var(--navy)" points="778,0 790,0 -122,686 -134,686"/>
      <polygon fill="var(--lime-bright)" points="806,0 866,0 -46,686 -106,686"/>
      <polygon fill="var(--lime-bright)" points="1745,0 1800,0 888,686 833,686"/>
    </svg>

    <div class="brand">
      <div class="brand-dot"></div>
      <div class="brand-name">LARKVALE<span>RESIDENCES</span></div>
    </div>

    <div class="contact">
      <p class="contact-heading">Contact Address:</p>
      <p class="contact-address">48 fenwick lane, Dallas</p>
      <p class="contact-phone">+15550142290</p>
    </div>

    <div class="website">www.larkvale.com</div>
  </div>
</body>
</html>
```